Professional Home Buyer business card needed

I need a pretty straight forward business card designed. We help people that NEED to sell their homes solve problems. We perform all types of Real Estate transactions including flip, wholesale, investment, rental property and multi family. The card will mainly be used to give to prospective Sellers but will also be given to Real Estate Investors as well. It should professional and very easy to read, most clients are older people.

Target Market(s)

Distressed home sellers as well as Real Estate investors

Industry/Entity Type

Real Estate

Contact Information for Business Card

should be a professional layout

Colors
ec1f27
ffffff
000000

Requirements
Must have
• Large logo on back and smaller one on front. should utilize Red, white, and black.
• I am thinking of using a soft touch coating on the card so keep that in mind.
• Contact info should be very easy to read, think older clients.
Nice to have
• I would like to see a design with rounded corners on the card
Should not have
• pictures of homes or other home graphics.

```html
<!DOCTYPE html>
<html lang="en">
<head>
<meta charset="utf-8">
<title>Keystone Home Buyers – Business Card</title>
<link href="https://fonts.googleapis.com/css2?family=Oxygen:wght@400;700&display=swap" rel="stylesheet">
<style>
  :root {
    --red: #ec1f27;
    --black: #000000;
    --white: #ffffff;
    --card-dark: #1a1a1a;
    --stage: #f5f5f5;
    --logo-grey: #6e6e6e;
  }
  * { box-sizing: border-box; margin: 0; padding: 0; }
  html, body { width: 1200px; height: 1000px; overflow: hidden; }
  body {
    background: var(--stage);
    font-family: "Oxygen", Arial, sans-serif;
    position: relative;
  }
  .card {
    position: absolute;
    border-radius: 22px;
    overflow: hidden;
    box-shadow: 0 14px 30px rgba(0,0,0,0.18);
  }
  .card::after {
    content: "";
    position: absolute;
    left: 0; right: 0; bottom: 0;
    height: 8px;
    background: var(--red);
  }
  .card-back {
    left: 265px; top: 90px; width: 670px; height: 382px;
    background: var(--card-dark);
    display: flex; align-items: center; justify-content: center;
  }
  .brand-large {
    color: var(--logo-grey);
    font-weight: 700;
    text-align: center;
    font-size: 58px;
    line-height: 1.05;
    letter-spacing: 2px;
    text-transform: uppercase;
  }
  .card-front {
    left: 262px; top: 525px; width: 676px; height: 385px;
    background: var(--white);
  }
  .brand-small {
    position: absolute;
    left: 52px; top: 158px; width: 222px;
    color: var(--black);
    font-weight: 700;
    text-align: center;
    font-size: 30px;
    line-height: 1.1;
    text-transform: uppercase;
    letter-spacing: 1px;
  }
  .divider {
    position: absolute;
    left: 315px; top: 105px;
    width: 1px; height: 178px;
    background: var(--red);
  }
  .details {
    position: absolute;
    left: 349px; top: 100px;
  }
  .person-name {
    color: var(--red);
    font-weight: 700;
    font-size: 25px;
    line-height: 1.1;
  }
  .person-title {
    font-size: 16px;
    color: var(--black);
    margin-top: 2px;
  }
  .address {
    color: var(--red);
    font-size: 16px;
    line-height: 21px;
    margin-top: 9px;
  }
  .contacts { list-style: none; margin-top: 10px; }
  .contacts li {
    display: flex; align-items: center;
    font-size: 16px;
    height: 27px;
    color: var(--black);
  }
  .contacts svg { width: 19px; height: 19px; margin-right: 9px; fill: var(--red); }
</style>
</head>
<body>
  <section class="card card-back">
    <div class="brand-large">Keystone<br>Home Buyers</div>
  </section>

  <section class="card card-front">
    <div class="brand-small">Keystone<br>Home Buyers</div>
    <div class="divider"></div>
    <div class="details">
      <div class="person-name">Dale Morrow</div>
      <div class="person-title">President</div>
      <div class="address">P.O. Box 12<br>Fairview, KS 67000</div>
      <ul class="contacts">
        <li>
          <svg viewBox="0 0 24 24" aria-hidden="true"><path d="M6.6 10.8a15.1 15.1 0 0 0 6.6 6.6l2.2-2.2c.3-.3.7-.4 1-.2 1.1.4 2.3.6 3.6.6.6 0 1 .4 1 1V20c0 .6-.4 1-1 1C10.6 21 3 13.4 3 4c0-.6.4-1 1-1h3.5c.6 0 1 .4 1 1 0 1.3.2 2.5.6 3.6.1.3 0 .7-.2 1z"/></svg>
          555 - 014 - 2280
        </li>
        <li>
          <svg viewBox="0 0 24 24" aria-hidden="true"><path d="M2 5h20v2l-10 6L2 7z M2 9l10 6 10-6v10H2z"/></svg>
          dale@prairiehomesforcash.com
        </li>
        <li>
          <svg viewBox="0 0 24 24" aria-hidden="true"><path d="M12 2a10 10 0 1 0 0 20 10 10 0 0 0 0-20zm0 2c1 0 2 .2 2.9.6L13 7l-3-1-2 2 1 3-3 2-2-1A8 8 0 0 1 12 4zm-1 15.9A8 8 0 0 1 4.3 14l2.7.9 2 3zm3-1.9-1-3 3-2 3 1a8 8 0 0 1-5 6z"/></svg>
          www.prairiehomesforcash.com
        </li>
      </ul>
    </div>
  </section>
</body>
</html>
```